R7M Horizon Business Card Design

We need a business card created for our New Business "R7M Horizon"<br/><br/>The business card design is up to you however the following information must be on the business card:<br/><br/>Front of the business card -<br/>Email :tobyw@r7mhorizon.nz<br/>Mobile: +64 (0) 22 4871 569<br/>Website: www.r7mhorizon.nz<br/>Card Owner Name: Tobias Wrenhall<br/>Company Title: Business Development Manager<br/>Slogan: "The BEST of both worlds". <br/>Logo On the front attached to the design brief<br/><br/>On the back: <br/>Space on the back for 4 more versions of the logo across the bottom of the card indicating different subsidiary brands - R7M Coffee, R7M Arts, R7M ?? (The card will be used for all of these brands - We Will add the extra subsidiary logos to the design once the design is finished (We are a graphics design team). <br/><br/>Other than that we want a premium feeling logo that remains universally usable depending on the business entity that we are using the card for. The use of bright bold colours would be great but we still want the card to feel premium.
Target Market(s)
Gift Design and Manufacturing Companies
Contact Information for Business Card
Front of the business card -
Email :tobyw@r7mhorizon.nz
Mobile: +64 (0) 22 4871 569
Website: www.r7mhorizon.nz
Card Owner Name: Tobias Wrenhall
Company Title: Business Development Manager
Slogan: "The BEST of both worlds".
Logo On the front attached to the design brief

```html
<!DOCTYPE html>
<html lang="en">
<head>
<meta charset="utf-8">
<title>R7M Horizon Business Card</title>
<link href="https://fonts.googleapis.com/css2?family=Exo+2:wght@400;600;700&family=Open+Sans:wght@400;500&display=swap" rel="stylesheet">
<style>
  :root{
    --stage:#1c1c1e;
    --card:#242527;
    --card-edge:#3b4bc4;
    --brand-blue:#3f4fc8;
    --ink-white:#f2f2f2;
    --faint-ring:#2c2f44;
    --divider:#e8e8e8;
  }
  *{margin:0;padding:0;box-sizing:border-box}
  html,body{width:1200px;height:900px;overflow:hidden}
  body{
    background:radial-gradient(ellipse at 50% 30%, #2e2e31 0%, var(--stage) 70%);
    font-family:"Open Sans", sans-serif;
    position:relative;
  }
  .card{
    position:absolute;
    left:250px;
    width:700px;
    height:400px;
    background:var(--card);
    border-left:4px solid var(--card-edge);
    border-bottom:4px solid var(--card-edge);
    box-shadow:0 14px 30px rgba(0,0,0,.55);
    overflow:hidden;
  }
  .card--back{top:36px}
  .card--front{top:466px}

  /* back */
  .back-ring{
    position:absolute;left:50%;top:50%;
    width:330px;height:330px;margin:-165px 0 0 -165px;
    border:8px solid var(--faint-ring);border-radius:50%;
  }
  .back-name{
    position:absolute;left:0;right:0;top:50%;transform:translateY(-50%);
    text-align:center;
    font-family:"Exo 2", sans-serif;font-weight:700;font-size:46px;
    color:#3a3b3e;letter-spacing:1px;
  }

  /* front */
  .brand{
    position:absolute;left:70px;top:118px;
    display:flex;align-items:center;gap:14px;
  }
  .brand-ring{
    width:92px;height:92px;border:9px solid var(--brand-blue);border-radius:50%;
  }
  .brand-name{
    font-family:"Exo 2", sans-serif;font-weight:700;font-size:34px;line-height:1.05;
    color:var(--brand-blue);
  }
  .divider{
    position:absolute;left:385px;width:2px;background:var(--divider);
  }
  .divider--top{top:120px;height:38px}
  .divider--bottom{top:178px;height:92px}
  .details{position:absolute;left:410px;top:112px}
  .person-name{
    font-family:"Exo 2", sans-serif;font-weight:700;font-size:26px;
    color:var(--brand-blue);text-transform:uppercase;letter-spacing:.5px;line-height:1;
  }
  .person-title{font-size:17px;color:var(--ink-white);margin-top:4px}
  .contacts{list-style:none;margin-top:16px}
  .contacts li{
    display:flex;align-items:center;gap:12px;
    font-size:19px;color:var(--ink-white);letter-spacing:.6px;line-height:28px;
  }
  .contacts svg{width:18px;height:18px;flex:none}
  .slogan{
    position:absolute;left:392px;top:302px;
    font-family:"Exo 2", sans-serif;font-weight:400;font-size:21px;
    color:var(--brand-blue);text-transform:uppercase;letter-spacing:.4px;
  }
</style>
</head>
<body>

<section class="card card--back">
  <div class="back-ring"></div>
  <div class="back-name">R7M Horizon</div>
</section>

<section class="card card--front">
  <div class="brand">
    <div class="brand-ring"></div>
    <div class="brand-name">R7M<br>Horizon</div>
  </div>

  <span class="divider divider--top"></span>
  <span class="divider divider--bottom"></span>

  <div class="details">
    <h1 class="person-name">Tobias Wrenhall</h1>
    <p class="person-title">Business Development Manager</p>
    <ul class="contacts">
      <li>
        <svg viewBox="0 0 20 20" fill="none" stroke="#3f4fc8" stroke-width="1.6"><circle cx="10" cy="10" r="8.5"/><path d="M7 6l1.5 2.5-1 1a5 5 0 003 3l1-1L14 13l-1 1.5C9 14 6 11 5.8 7z" fill="#3f4fc8" stroke="none"/></svg>
        +64 (0) 22 4871 569
      </li>
      <li>
        <svg viewBox="0 0 20 20" fill="none" stroke="#3f4fc8" stroke-width="1.6"><rect x="2" y="4.5" width="16" height="11" rx="1"/><path d="M2.5 5l7.5 6 7.5-6"/></svg>
        tobyw@r7mhorizon.nz
      </li>
      <li>
        <svg viewBox="0 0 20 20" fill="none" stroke="#3f4fc8" stroke-width="1.6"><circle cx="10" cy="10" r="8.5"/><ellipse cx="10" cy="10" rx="3.6" ry="8.5"/><path d="M1.5 10h17M3 5.5h14M3 14.5h14"/></svg>
        www.r7mhorizon.nz
      </li>
    </ul>
  </div>

  <p class="slogan">The best of both worlds</p>
</section>

</body>
</html>
```